Brit Rock covers band "The Tin Kettles" requires poster for Fernhollow Club Friday March 31st

I want a design for a poster (A3 and A4) and Social media ads.
Primary focus is the band name logo "The Tin Kettles", style as in attached file, followed by tag "Old Skool Brit Rock".
Backdrop to be 60's psychedelic art.
Secondary focus is the venue "The Fernhollow Club"
Supporting text to include:
- 27 Quill Street, Chatswood SYDNEY
- Friday 31st March 2023
- 7:00 pm until late
- Bar sales refreshments
- NO admission fee

```html
<!DOCTYPE html>
<html lang="en">
<head>
<meta charset="utf-8">
<title>The Tin Kettles – Old Skool Brit Rock – Poster Set</title>
<link rel="stylesheet" href="https://fonts.googleapis.com/css2?family=Oswald:wght@400;500;700&family=Fira+Sans:wght@300;700;800&family=Archivo:wght@700&display=swap">
<style>
  :root {
    --board: #7a7a7a;
    --navy: #2b3d5d;
    --red: #bf4437;
    --cream: #e3dcd8;
    --ink: #111111;
    --paper: #f4f4f4;
    --swirl-a: #f7f7f7;
    --swirl-b: #d9d9d9;
    --white: #ffffff;
    --label: #f2f2f2;
  }
  * { box-sizing: border-box; margin: 0; padding: 0; }
  html, body { width: 1200px; height: 1185px; overflow: hidden; }
  body { background: var(--board); position: relative; font-family: "Oswald", sans-serif; }

  .poster { position: absolute; overflow: hidden; background: var(--paper); }
  .poster--a4 { left: 147px; top: 60px; width: 424px; height: 600px; }
  .poster--a3 { left: 628px; top: 60px; width: 425px; height: 600px; }
  .poster--social { left: 397px; top: 726px; width: 405px; height: 404px; }

  .poster__backdrop {
    position: absolute; inset: 0;
    background: radial-gradient(ellipse at 30% 60%, var(--swirl-b) 0%, var(--swirl-a) 45%, var(--swirl-b) 75%, var(--swirl-a) 100%);
  }

  .band { position: absolute; left: 0; right: 0; display: flex; align-items: center; justify-content: center; text-align: center; }

  .date-band { top: 0; }
  .date {
    font-family: "Fira Sans", sans-serif; font-weight: 700; color: var(--red);
    font-size: 27px; letter-spacing: 0.2px;
  }

  .headline-band { background: var(--navy); flex-direction: column; }
  .headline {
    font-family: "Oswald", sans-serif; font-weight: 700; color: var(--cream);
    font-size: 74px; line-height: 1.02; text-shadow: 3px 3px 0 #16223a;
    letter-spacing: 1px;
  }

  .act-band { flex-direction: column; }
  .act-name {
    font-family: "Oswald", sans-serif; font-weight: 700; color: var(--ink);
    font-size: 80px; line-height: 0.95; text-transform: uppercase;
  }

  .venue-band { background: var(--red); }
  .venue {
    font-family: "Fira Sans", sans-serif; font-weight: 800; color: var(--white);
    font-size: 25px; letter-spacing: 0.5px;
  }

  .info-band { background: var(--navy); display: grid; grid-template-columns: 1.45fr 0.72fr 1fr 1.22fr; padding: 0 20px 0 16px; }
  .info-item {
    color: var(--white); font-family: "Oswald", sans-serif; font-weight: 400;
    font-size: 15px; line-height: 1.22; display: flex; align-items: center; justify-content: center;
    height: 70%; align-self: center;
  }
  .info-item + .info-item { border-left: 1px solid rgba(255,255,255,0.75); }

  /* A4 */
  .poster--a4 .date-band { height: 75px; padding-top: 8px; }
  .poster--a4 .headline-band { top: 75px; height: 184px; }
  .poster--a4 .act-band { top: 259px; height: 238px; }
  .poster--a4 .venue-band { top: 497px; height: 37px; }
  .poster--a4 .info-band { top: 534px; height: 55px; }

  /* A3 */
  .poster--a3 .date-band { height: 67px; padding-bottom: 2px; }
  .poster--a3 .headline-band { top: 67px; height: 183px; }
  .poster--a3 .act-band { top: 250px; height: 247px; }
  .poster--a3 .venue-band { top: 497px; height: 36px; }
  .poster--a3 .info-band { top: 533px; height: 58px; }

  /* Social square */
  .poster--social .date-band { height: 53px; padding-top: 2px; }
  .poster--social .date { font-size: 26px; }
  .poster--social .headline-band { top: 53px; height: 125px; }
  .poster--social .headline { font-family: "Archivo", sans-serif; font-size: 52px; line-height: 1.06; text-shadow: none; letter-spacing: 0; }
  .poster--social .act-band { top: 178px; height: 139px; }
  .poster--social .act-name { font-size: 50px; }
  .poster--social .venue-band { top: 317px; height: 29px; }
  .poster--social .venue { font-size: 20px; letter-spacing: 0.8px; }
  .poster--social .info-band { top: 346px; height: 51px; padding: 0 18px 0 10px; }
  .poster--social .info-item { font-size: 13.5px; }

  .format-label {
    position: absolute; color: var(--label); font-family: "Fira Sans", sans-serif; font-weight: 300;
    font-size: 22px; line-height: 1; text-align: center; letter-spacing: 0.3px;
  }
  .format-label--a4 { left: 147px; top: 674px; width: 424px; }
  .format-label--a3 { left: 628px; top: 674px; width: 425px; }
  .format-label--social { left: 397px; top: 1143px; width: 405px; }
</style>
</head>
<body>

  <article class="poster poster--a4">
    <div class="poster__backdrop" role="img" aria-label="60s psychedelic swirl pattern in soft greys"></div>
    <div class="band date-band"><p class="date">FRIDAY 31st MARCH 2023</p></div>
    <div class="band headline-band"><h1 class="headline">OLD SKOOL<br>BRIT ROCK</h1></div>
    <div class="band act-band"><p class="act-name">The Tin<br>Kettles</p></div>
    <div class="band venue-band"><p class="venue">THE FERNHOLLOW CLUB</p></div>
    <div class="band info-band">
      <p class="info-item">27 Quill Street,<br>Chatswood SYDNEY</p>
      <p class="info-item">7:00 pm<br>until late</p>
      <p class="info-item">Bar sales<br>refreshments</p>
      <p class="info-item">NO<br>ADMISSION FEE</p>
    </div>
  </article>
  <p class="format-label format-label--a4">A4</p>

  <article class="poster poster--a3">
    <div class="poster__backdrop" role="img" aria-label="60s psychedelic swirl pattern in soft greys"></div>
    <div class="band date-band"><p class="date">FRIDAY 31st MARCH 2023</p></div>
    <div class="band headline-band"><h1 class="headline">OLD SKOOL<br>BRIT ROCK</h1></div>
    <div class="band act-band"><p class="act-name">The Tin<br>Kettles</p></div>
    <div class="band venue-band"><p class="venue">THE FERNHOLLOW CLUB</p></div>
    <div class="band info-band">
      <p class="info-item">27 Quill Street,<br>Chatswood SYDNEY</p>
      <p class="info-item">7:00 pm<br>until late</p>
      <p class="info-item">Bar sales<br>refreshments</p>
      <p class="info-item">NO<br>ADMISSION FEE</p>
    </div>
  </article>
  <p class="format-label format-label--a3">A3</p>

  <article class="poster poster--social">
    <div class="poster__backdrop" role="img" aria-label="60s psychedelic swirl pattern in soft greys"></div>
    <div class="band date-band"><p class="date">FRIDAY 31st MARCH 2023</p></div>
    <div class="band headline-band"><h1 class="headline">OLD SKOOL<br>BRIT ROCK</h1></div>
    <div class="band act-band"><p class="act-name">The Tin<br>Kettles</p></div>
    <div class="band venue-band"><p class="venue">THE FERNHOLLOW CLUB</p></div>
    <div class="band info-band">
      <p class="info-item">27 Quill Street,<br>Chatswood SYDNEY</p>
      <p class="info-item">7:00 pm<br>until late</p>
      <p class="info-item">Bar sales<br>refreshments</p>
      <p class="info-item">NO<br>admission fee</p>
    </div>
  </article>
  <p class="format-label format-label--social">Social media ads</p>

</body>
</html>
```